Brightfold Partners Website

Brightfold Partners (BP) provide Analytics & Enterprise Performance Management (EPM) advisory & consultancy services. We are passionate about data and making a difference for our clients by working in partnership with them, helping them on their journey to becoming an Brightfold Partner. We deliver insights which give our clients a competitive edge and a much deeper understanding of their organisation.

We need a website which shows who we are, what we do and how we do it.

www.brightfold-partners.example is our very basic website at the moment. We want to completely revamp it with a corporate look

```html
<!DOCTYPE html>
<html lang="en">
<head>
<meta charset="utf-8">
<title>Brightfold Partners</title>
<link href="https://fonts.googleapis.com/css2?family=Red+Hat+Display:wght@500;600;700&family=Nunito+Sans:wght@400;600;700&display=swap" rel="stylesheet">
<style>
:root{
  --navy:#2a5370;
  --navy-deep:#1e3f58;
  --orange:#f07c0d;
  --ink:#1b1b1b;
  --text:#333;
  --muted:#888;
  --light:#f4f4f4;
  --footer:#1c1c1c;
  --white:#fff;
}
*{box-sizing:border-box;margin:0;padding:0}
html,body{width:1200px;height:3420px;overflow:hidden}
body{font-family:"Nunito Sans",Arial,sans-serif;color:var(--text);background:var(--white);position:relative}
.abs{position:absolute}
h1,h2,h3,.head{font-family:"Red Hat Display","Nunito Sans",sans-serif}

/* header */
.header{top:0;left:0;width:1200px;height:115px;background:var(--white)}
.brand{display:flex;align-items:center;gap:14px;font-family:"Red Hat Display",sans-serif;font-weight:700;font-size:24px;line-height:26px;letter-spacing:1px;color:var(--navy)}
.brand .mark{width:62px;height:62px;border-radius:50%;border:9px solid var(--navy)}
.contact-chip{display:flex;align-items:center;gap:12px;font-size:15px;color:var(--ink)}
.contact-chip small{display:block;font-size:13px;color:#666}
.chip-icon{width:42px;height:42px;border-radius:50%;background:var(--navy);display:flex;align-items:center;justify-content:center}
.login{top:12px;left:975px;width:114px;height:42px;background:var(--white);border-radius:22px;box-shadow:0 2px 8px rgba(0,0,0,.15);display:flex;align-items:center;gap:10px;font-weight:700;font-size:17px;color:var(--ink)}
.nav{top:77px;left:378px;width:822px;height:53px;background:var(--navy);clip-path:polygon(22px 0,100% 0,100% 100%,0 100%)}
.nav a{position:absolute;top:16px;color:var(--white);font-size:15px;text-decoration:none}
.nav a.active{color:var(--orange)}
.nav .phone{display:flex;align-items:center;gap:12px;position:absolute;left:514px;top:9px;color:var(--white);font-size:16px}
.nav .phone span.dot{width:34px;height:34px;border-radius:50%;background:var(--orange);display:flex;align-items:center;justify-content:center}

/* hero */
.hero{top:115px;left:0;width:1200px;height:686px;overflow:hidden;
  background:
    radial-gradient(ellipse 260px 60px at 930px 500px,rgba(255,90,60,.75),rgba(255,140,40,.35) 50%,transparent 80%),
    radial-gradient(ellipse 300px 40px at 1050px 570px,rgba(255,200,120,.55),transparent 75%),
    radial-gradient(ellipse 220px 420px at 870px 220px,rgba(130,160,190,.55),transparent 70%),
    radial-gradient(ellipse 180px 380px at 1060px 230px,rgba(150,175,200,.5),transparent 70%),
    radial-gradient(ellipse 260px 460px at 140px 120px,rgba(90,110,130,.45),transparent 70%),
    linear-gradient(180deg,rgba(0,0,0,0) 60%,rgba(10,14,20,.7) 100%),
    linear-gradient(100deg,#121a24 0%,#1f2c3a 35%,#3c5064 60%,#5f7487 80%,#7d8e9c 100%)}
.hero-ring{left:520px;top:155px;width:900px;height:900px;border-radius:50%;background:rgba(150,175,200,.16);border:1px solid rgba(255,255,255,.12)}
.hero-shade{left:0;top:115px;width:700px;height:686px;background:linear-gradient(90deg,rgba(8,12,18,.55),rgba(8,12,18,0))}
.hero-text{left:110px;top:294px;color:var(--white)}
.hero-text .welcome{font-size:22px}
.hero-text h1{font-size:72px;line-height:68px;font-weight:600;margin-top:14px}
.hero-text p{font-size:22px;margin-top:14px}
.btn-orange{display:inline-block;margin-top:28px;width:164px;height:58px;line-height:58px;text-align:center;border-radius:30px;background:var(--orange);color:var(--white);font-weight:700;font-size:16px}

/* section titles */
.title{width:1200px;left:0;text-align:center;font-size:35px;font-weight:600;color:var(--ink)}
.title::after{content:"";display:block;width:62px;height:4px;background:var(--navy);margin:12px auto 0}
.lead{left:190px;width:820px;text-align:center;font-size:15px;line-height:26px;color:var(--text)}

/* services */
.service{width:260px;text-align:center}
.ring{width:226px;height:226px;border-radius:50%;border:3px dotted var(--navy);margin:0 auto;display:flex;align-items:center;justify-content:center}
.ring.orange{border-color:var(--orange)}
.disc{width:204px;height:204px;border-radius:50%;background:var(--navy);display:flex;align-items:center;justify-content:center}
.ring.orange .disc{background:var(--orange)}
.service h3{font-size:25px;font-weight:600;color:var(--ink);margin-top:22px;line-height:32px}

/* how */
.how{top:1447px;left:0;width:1200px;height:571px;background:var(--light)}
.card{top:1660px;width:387px;height:276px;overflow:visible}
.card .label{position:absolute;left:0;top:140px;padding:8px 11px;font-family:"Red Hat Display",sans-serif;font-weight:600;font-size:20px;line-height:26px;color:var(--white);white-space:nowrap}
.label.navy{background:rgba(42,83,112,.85);width:250px}
.label.orange{background:rgba(240,124,13,.9);width:225px}
.card-a{left:13px;background:
  radial-gradient(ellipse 70px 90px at 195px 75px,rgba(220,190,160,.8),transparent 75%),
  radial-gradient(ellipse 90px 150px at 200px 210px,rgba(40,40,48,.85),transparent 75%),
  radial-gradient(ellipse 80px 140px at 70px 180px,rgba(70,65,60,.8),transparent 75%),
  linear-gradient(90deg,#5d574f,#a59a8a 40%,#c9c3b8 75%,#6a6660)}
.card-b{left:411px;background:
  radial-gradient(ellipse 60px 80px at 230px 70px,rgba(230,200,175,.8),transparent 75%),
  radial-gradient(ellipse 120px 90px at 300px 200px,rgba(40,38,40,.85),transparent 75%),
  radial-gradient(ellipse 80px 90px at 110px 70px,rgba(200,205,210,.75),transparent 75%),
  linear-gradient(160deg,#4d5357,#9c968c 45%,#d8d2c8 70%,#3f3c3a)}
.card-c{left:808px;background:
  radial-gradient(ellipse 170px 40px at 200px 215px,rgba(120,80,55,.9),transparent 80%),
  radial-gradient(ellipse 50px 90px at 300px 110px,rgba(45,40,45,.8),transparent 75%),
  radial-gradient(ellipse 50px 90px at 120px 110px,rgba(60,55,55,.75),transparent 75%),
  linear-gradient(180deg,#e6e8e6,#c4c4bf 45%,#8a7a6c 80%,#5b4a3c)}

/* who */
.who{top:2018px;left:0;width:1200px;height:522px;background:
  radial-gradient(ellipse 180px 200px at 900px 150px,rgba(110,140,165,.35),transparent 75%),
  radial-gradient(ellipse 200px 160px at 120px 320px,rgba(70,100,125,.45),transparent 75%),
  linear-gradient(90deg,#2c4d66,#3d6380 55%,#335a77)}
.who-circle{left:80px;top:2047px;width:460px;height:460px;border-radius:50%;background:
  radial-gradient(ellipse 70px 90px at 300px 110px,rgba(225,200,180,.55),transparent 75%),
  radial-gradient(ellipse 60px 80px at 110px 100px,rgba(210,185,165,.45),transparent 75%),
  radial-gradient(ellipse 140px 60px at 250px 370px,rgba(235,225,215,.45),transparent 75%),
  radial-gradient(ellipse 100px 160px at 330px 260px,rgba(40,70,95,.6),transparent 75%),
  linear-gradient(135deg,#9cb2c3,#5c7f9a 55%,#3a5c77)}
.who-line{left:586px;top:2094px;width:3px;height:378px;background:var(--white)}
.who-text{left:622px;top:2104px;width:470px;color:var(--white)}
.who-text h2{font-size:35px;font-weight:600}
.who-text p{font-size:15.5px;line-height:26px;margin-top:10px}
.btn-white{display:inline-block;margin-top:24px;width:168px;height:52px;line-height:52px;text-align:center;border-radius:26px;background:var(--white);color:var(--navy);font-weight:700;font-size:16px}

/* contact */
.info{left:113px;display:flex;gap:16px;width:300px}
.info .ico{width:52px;height:52px;border-radius:50%;border:2px solid var(--navy);flex:none;display:flex;align-items:center;justify-content:center}
.info h4{font-family:"Red Hat Display",sans-serif;font-size:21px;font-weight:600;color:var(--ink)}
.info p{font-size:15px;line-height:24px;color:var(--ink)}
.field{left:437px;width:318px;height:54px;background:var(--white);box-shadow:0 2px 12px rgba(0,0,0,.08);font-size:15px;color:var(--muted);padding:17px 24px}
.submit{left:436px;top:2918px;width:319px;height:54px;background:var(--navy);color:var(--white);font-weight:700;font-size:16px;text-align:center;line-height:54px}
.message{left:775px;top:2712px;width:300px;height:258px;background:var(--white);box-shadow:0 2px 12px rgba(0,0,0,.08);font-size:15px;color:var(--muted);padding:17px 24px}

/* footer */
.footer{top:3048px;left:0;width:1200px;height:372px;background:var(--footer);color:var(--white)}
.f-brand{left:113px;top:3118px;display:flex;align-items:center;gap:16px;font-family:"Red Hat Display",sans-serif;font-weight:700;font-size:25px;line-height:27px;letter-spacing:1px;color:var(--white)}
.f-brand .mark{width:66px;height:66px;border-radius:50%;border:10px solid var(--white)}
.socials{left:180px;top:3215px;display:flex;gap:8px}
.socials span{width:31px;height:31px;border-radius:50%;background:var(--white)}
.f-col{top:3110px;color:var(--white)}
.f-col h5{font-family:"Red Hat Display",sans-serif;font-size:20px;font-weight:600}
.f-col h5::after{content:"";display:block;width:38px;height:3px;background:var(--orange);margin-top:10px}
.f-col ul{list-style:none;margin-top:12px}
.f-col li{font-size:15px;line-height:30px}
.f-col p{font-size:15px;line-height:26px;margin-top:12px;width:290px}
.subscribe{left:805px;top:3231px;width:275px;height:42px;background:var(--white);border-radius:22px;font-size:15px;color:#999;padding:11px 20px}
.send{left:1033px;top:3230px;width:46px;height:46px;border-radius:50%;background:var(--navy);display:flex;align-items:center;justify-content:center}
.f-rule{left:113px;top:3316px;width:978px;height:1px;background:#3a3a3a}
.copy{left:0;top:3360px;width:1200px;text-align:center;font-size:15px;color:var(--white)}
</style>
</head>
<body>

<header class="header abs">
  <div class="brand abs" style="left:110px;top:20px"><span class="mark"></span><span>BRIGHTFOLD<br>PARTNERS</span></div>
  <div class="contact-chip abs" style="left:420px;top:12px">
    <span class="chip-icon"><svg width="18" height="14" viewBox="0 0 18 14"><rect x="1" y="1" width="16" height="12" rx="2" fill="#fff"/><path d="M1 2l8 6 8-6" stroke="#2a5370" stroke-width="2" fill="none"/></svg></span>
    <div>Send Us Email<small>info@brightfold-partners.example</small></div>
  </div>
  <div class="contact-chip abs" style="left:715px;top:12px">
    <span class="chip-icon"><svg width="16" height="20" viewBox="0 0 16 20"><path d="M8 0a8 8 0 0 1 8 8c0 6-8 12-8 12S0 14 0 8a8 8 0 0 1 8-8z" fill="#fff"/><circle cx="8" cy="8" r="3" fill="#2a5370"/></svg></span>
    <div>Location<small>Lorem ipsum dolor sit amet,</small></div>
  </div>
  <div class="login abs"><span class="chip-icon" style="width:40px;height:40px"><svg width="16" height="16" viewBox="0 0 16 16"><circle cx="8" cy="5" r="4" fill="#fff"/><path d="M0 16c0-5 4-7 8-7s8 2 8 7z" fill="#fff"/></svg></span>Login</div>
  <nav class="nav abs">
    <a class="active" style="left:58px">Home</a>
    <a style="left:155px">Services</a>
    <a style="left:268px">About Us</a>
    <a style="left:386px">Contact Us</a>
    <div class="phone"><span class="dot"><svg width="14" height="14" viewBox="0 0 14 14"><path d="M3 0l3 3-2 2c1 2 3 4 5 5l2-2 3 3-2 3C6 14 0 8 0 3z" fill="#fff"/></svg></span>01 555 0142</div>
  </nav>
</header>

<section class="hero abs" role="img" aria-label="Dusk city skyline of glass towers with light trails on a road">
  <div class="hero-ring abs" style="left:520px;top:40px"></div>
</section>
<div class="hero-shade abs"></div>
<div class="hero-text abs">
  <div class="welcome">Welcome To</div>
  <h1>Brightfold<br>Partners</h1>
  <p>Data Analytics &amp; Epm Consulting Services</p>
  <span class="btn-orange">Get Started</span>
</div>

<h2 class="title abs" style="top:862px">What We Do</h2>
<p class="lead abs" style="top:949px">Lorem ipsum dolor sit amet, consectetur adipiscing elit, sed do eiusmod tempor incididunt ut labore et dolore magna aliqua. Quis ipsum suspendisse ultrices gravida. Risus commodo viverra maecenas accumsan lacus vel facilisis. Lorem ipsum dolor sit amet, consectetur adipiscing elit</p>

<div class="service abs" style="left:156px;top:1058px">
  <div class="ring"><div class="disc">
    <svg width="110" height="100" viewBox="0 0 110 100" fill="none" stroke="#fff" stroke-width="3"><rect x="30" y="8" width="50" height="32" rx="6"/><path d="M42 40l-6 10 14-10"/><circle cx="45" cy="24" r="1.5" fill="#fff"/><circle cx="55" cy="24" r="1.5" fill="#fff"/><circle cx="65" cy="24" r="1.5" fill="#fff"/><rect x="10" y="62" width="14" height="24"/><path d="M24 66h24c6 0 8 6 2 8H38m-14 10h30l36-20c4-3 0-8-4-6L62 70"/></svg>
  </div></div>
  <h3>Advise &amp; Architect<br>Services</h3>
</div>
<div class="service abs" style="left:474px;top:1058px">
  <div class="ring orange"><div class="disc">
    <svg width="110" height="100" viewBox="0 0 110 100" fill="none" stroke="#fff" stroke-width="3"><path d="M14 18h8v66h-8zM22 22h60v30M22 84h40"/><path d="M44 70l36-40 8 7-36 40-10 3z"/><path d="M60 88l30-30v30z"/><path d="M76 82h8v-8z"/></svg>
  </div></div>
  <h3>Design &amp; implement</h3>
</div>
<div class="service abs" style="left:790px;top:1058px">
  <div class="ring"><div class="disc">
    <svg width="110" height="110" viewBox="0 0 110 110" fill="none" stroke="#fff" stroke-width="3"><circle cx="52" cy="58" r="40"/><circle cx="52" cy="58" r="28"/><circle cx="52" cy="58" r="16"/><circle cx="52" cy="58" r="5"/><path d="M52 58l38-38M80 20l10-2-2 10 8-2-8 8-8 2"/></svg>
  </div></div>
  <h3>Optimise &amp; Manage</h3>
</div>

<section class="how abs"></section>
<h2 class="title abs" style="top:1481px">How We Do It</h2>
<p class="lead abs" style="top:1553px">Lorem ipsum dolor sit amet, consectetur adipiscing elit, sed do eiusmod tempor incididunt ut labore et dolore magna aliqua. Quis ipsum suspendisse ultrices gravida.</p>

<div class="card card-a abs" role="img" aria-label="Two businessmen talking in an office">
  <div class="label navy">Brightfold Partners (BP)<br>provide Analytics</div>
</div>
<div class="card card-b abs" role="img" aria-label="Team reviewing work at a desk with a monitor">
  <div class="label orange">Enterprise Performance<br>Management</div>
</div>
<div class="card card-c abs" role="img" aria-label="Colleagues stacking hands over a meeting table">
  <div class="label navy" style="top:150px;width:230px">Advisory &amp; Consultancy</div>
</div>

<section class="who abs" role="img" aria-label="Business people shaking hands, tinted in blue"></section>
<div class="who-circle abs" role="img" aria-label="Smiling colleagues shaking hands"></div>
<div class="who-line abs"></div>
<div class="who-text abs">
  <h2>Who We Are</h2>
  <p>Lorem ipsum dolor sit amet, consectetur adipiscing elit, sed do eiusmod tempor incididunt ut labore et dolore magna aliqua. Quis ipsum suspendisse ultrices gravida. Risus commodo viverra maecenas accumsan lacus vel facilisis. Lorem ipsum dolor sit amet, consectetur adipiscing elit, sed do eiusmod tempor incididunt ut labore et dolore magna aliqua. Quis ipsum suspendisse ultrices gravida. Risus commodo viverra maecenas accumsan lacus vel facilisis.</p>
  <span class="btn-white">Learn More</span>
</div>

<h2 class="title abs" style="top:2612px">Contact Us</h2>
<div class="info abs" style="top:2712px">
  <span class="ico"><svg width="14" height="18" viewBox="0 0 16 20"><path d="M8 0a8 8 0 0 1 8 8c0 6-8 12-8 12S0 14 0 8a8 8 0 0 1 8-8z" fill="#2a5370"/><circle cx="8" cy="8" r="3" fill="#fff"/></svg></span>
  <div><h4>Location</h4><p>19/B Brightfold Partners dolor sit amet, consectetur</p></div>
</div>
<div class="info abs" style="top:2817px">
  <span class="ico"><svg width="16" height="16" viewBox="0 0 14 14"><path d="M3 0l3 3-2 2c1 2 3 4 5 5l2-2 3 3-2 3C6 14 0 8 0 3z" fill="#2a5370"/></svg></span>
  <div><h4>Phone</h4><p>01 555 0142</p></div>
</div>
<div class="info abs" style="top:2912px;width:320px">
  <span class="ico"><svg width="16" height="12" viewBox="0 0 18 14"><rect x="1" y="1" width="16" height="12" rx="2" fill="#2a5370"/><path d="M1 2l8 6 8-6" stroke="#fff" stroke-width="2" fill="none"/></svg></span>
  <div><h4>Email</h4><p>info@brightfold-partners.example</p></div>
</div>
<div class="field abs" style="top:2712px">Name</div>
<div class="field abs" style="top:2780px">Phone</div>
<div class="field abs" style="top:2848px">Email</div>
<div class="submit abs">Submit</div>
<div class="message abs">Type your message</div>

<footer class="footer abs"></footer>
<div class="f-brand abs"><span class="mark"></span><span>BRIGHTFOLD<br>PARTNERS</span></div>
<div class="socials abs"><span></span><span></span><span></span><span></span></div>
<div class="f-col abs" style="left:421px"><h5>Quick Link</h5><ul><li>Home</li><li>Services</li><li>About Us</li><li>Contact Us</li></ul></div>
<div class="f-col abs" style="left:601px"><h5>Support</h5><ul><li>Terms &amp; Conditions</li><li>Privacy Policy</li><li>About Us</li><li>Support</li></ul></div>
<div class="f-col abs" style="left:804px"><h5>Subscribe To Our Newsletter</h5><p>Lorem ipsum dolor sit amet, consectetur adipiscing elit, sed do</p></div>
<div class="subscribe abs">Enter Your Email</div>
<div class="send abs"><svg width="18" height="18" viewBox="0 0 18 18"><path d="M17 1L1 8l6 2 2 6z" fill="#fff"/></svg></div>
<div class="f-rule abs"></div>
<div class="copy abs">©Copyrights 2022 Brightfold Partners &nbsp;&nbsp;|&nbsp;&nbsp; All Rights Reserved</div>

</body>
</html>
```